Kindling the Quiet Ember - Opening Doors to Brighter Days

I need a book cover front and back for this book. It is a self discovery book and will have a complementary transformation journal called Reshaping the Silver Compass. Id like the 2 covers to be in the same style as they will be sold together. So the winning design will get 2 covers from this project.
Here is a short statement about the book.......
As you begin the journey to: kindle the quiet ember, I know that it can feel lonely, but know that, as Dorian Vellacott sang much better than I can, "you are not alone, I am here with you." The journey may seem daunting but you are not walking this path alone. The path is worn down by the steps of those who have gone before. Allow me to encourage you, I'm not that far up the road ahead, we are traveling together.
This book will not provide all the answers, paths or tools needed for the journey, but it is a starting point. My Hope and desire is that this inspires, equips and gives the courage and strength to dig deep, to do the hard work and start to awaken the treasure within. The world needs that You. See you on the path!

```html
<!DOCTYPE html>
<html lang="en">
<head>
<meta charset="UTF-8">
<title>Kindling the Quiet Ember – Front Cover</title>
<link rel="stylesheet" href="https://fonts.googleapis.com/css2?family=Permanent+Marker&family=Oswald:wght@400;500;600;700&display=swap">
<style>
  :root {
    --backdrop: #c9d8e0;
    --sky-top: #eef0f1;
    --sky-mid: #dcdfe1;
    --grass-light: #a9b86a;
    --grass-deep: #5f7a34;
    --gold-deep: #a57d22;
    --gold-bright: #c99a35;
    --gold-soft: #d6c07a;
    --navy: #353d6b;
    --ink: #3b3d36;
    --paper-white: #ffffff;
  }
  * { margin: 0; padding: 0; box-sizing: border-box; }
  html, body {
    width: 1200px;
    height: 1182px;
    overflow: hidden;
    background: var(--backdrop);
  }
  .canvas {
    width: 1200px;
    height: 1182px;
    display: flex;
    align-items: center;
    justify-content: center;
  }
  .cover {
    position: relative;
    width: 700px;
    height: 1050px;
    overflow: hidden;
    background: var(--sky-top);
  }
  .cover-photo {
    position: absolute;
    inset: 0;
    background:
      radial-gradient(ellipse 45% 30% at 92% 78%, rgba(217,185,122,0.55), transparent 70%),
      linear-gradient(180deg, var(--sky-top) 0%, var(--sky-mid) 55%, #d3d6cf 72%, var(--grass-light) 86%, var(--grass-deep) 100%);
  }
  .hiker-area {
    position: absolute;
    left: 330px;
    top: 400px;
    width: 260px;
    height: 550px;
    border-radius: 120px 120px 20px 20px;
    background: linear-gradient(180deg, rgba(120,110,110,0.35), rgba(70,60,55,0.45));
  }
  .title-block {
    position: absolute;
    left: 40px;
    top: 120px;
    right: 30px;
  }
  .title { font-weight: normal; }
  .title-brush {
    display: block;
    font-family: 'Permanent Marker', cursive;
    font-size: 112px;
    line-height: 1.05;
    letter-spacing: -2px;
    white-space: nowrap;
    color: var(--gold-bright);
    background: linear-gradient(90deg, var(--gold-deep), var(--gold-bright) 60%, #b8892a);
    -webkit-background-clip: text;
    background-clip: text;
    -webkit-text-fill-color: transparent;
  }
  .title-line {
    display: block;
    margin-top: 4px;
    margin-left: 78px;
    font-family: 'Oswald', sans-serif;
    font-weight: 600;
    font-size: 74px;
    line-height: 1.05;
    text-transform: uppercase;
    letter-spacing: -1px;
    white-space: nowrap;
  }
  .title-soft { color: var(--gold-soft); }
  .title-strong { color: var(--navy); font-weight: 700; }
  .subtitle {
    margin-top: 22px;
    margin-left: 82px;
    font-family: 'Oswald', sans-serif;
    font-weight: 500;
    font-size: 22px;
    line-height: 1.35;
    text-transform: uppercase;
    color: var(--ink);
  }
  .author {
    position: absolute;
    left: 0;
    right: 0;
    bottom: 46px;
    text-align: center;
    font-family: 'Oswald', sans-serif;
    font-weight: 500;
    font-size: 44px;
    letter-spacing: 18px;
    text-transform: uppercase;
    color: var(--paper-white);
  }
</style>
</head>
<body>
  <main class="canvas">
    <section class="cover">
      <div class="cover-photo" role="img" aria-label="Photograph of a backpacker seen from behind, standing on a grassy hilltop under a pale sky with warm sunlight"></div>
      <div class="hiker-area" role="img" aria-label="Backpacker in a plaid shirt with a blue and grey rucksack looking into the distance"></div>

      <header class="title-block">
        <h1 class="title">
          <span class="title-brush">KINDLING</span>
          <span class="title-line"><span class="title-soft">The Quiet</span> <span class="title-strong">Ember</span></span>
        </h1>
        <p class="subtitle">Opening Doors<br>to Brighter Days</p>
      </header>

      <p class="author">Author Name</p>
    </section>
  </main>
</body>
</html>
```